facelift of our car wrap design - for Varno Klido L2

We would like to give our vehicles a facelift. Attached is our current advertising material.
Must-have: The paintwork of our vehicles is and will remain yellow. I would prefer to use the newer company logo, without the coloured bars, as shown in the attachment.
You can find further inspiration at www.plimtaaab.ch.

it should be a classic new design

• some advertising keywords

```html
<!DOCTYPE html>
<html lang="de">
<head>
<meta charset="utf-8">
<title>Plimtaaab – Fahrzeugbeschriftung Varno Klido L2</title>
<link rel="stylesheet" href="https://fonts.googleapis.com/css2?family=Poppins:wght@400;500;700;800&display=swap">
<style>
  :root {
    --backdrop: #e8e8e8;
    --paint-yellow: #e2c20e;
    --paint-shade: #d3b40a;
    --ink: #161616;
    --band-white: #ececec;
  }
  * { margin: 0; padding: 0; box-sizing: border-box; }
  html, body {
    width: 1200px; height: 1200px; overflow: hidden;
    background: var(--backdrop);
    font-family: "Poppins", sans-serif;
    color: var(--ink);
  }
  .sheet {
    width: 1200px; height: 1200px;
    display: flex; flex-direction: column; justify-content: center; gap: 80px;
    padding: 0 60px;
  }
  .wrap-panel {
    position: relative;
    height: 460px;
    background: linear-gradient(180deg, var(--paint-yellow) 0%, var(--paint-shade) 100%);
    border-radius: 18px;
    overflow: hidden;
  }
  .brand {
    position: absolute; left: 56px; top: 58px;
    display: flex; align-items: center; gap: 22px;
  }
  .brand-name {
    font-weight: 800; font-size: 112px; line-height: 1;
    letter-spacing: 2px;
  }
  .brand-dot {
    width: 70px; height: 70px; border-radius: 50%;
    background: var(--ink);
  }
  .contact {
    position: absolute; right: 70px; top: 218px;
    text-align: right;
  }
  .contact-phone {
    font-weight: 700; font-size: 42px; letter-spacing: 1px; line-height: 1.1;
  }
  .contact-web {
    font-weight: 500; font-size: 23px; line-height: 1.4;
  }
  .contact-web strong { font-weight: 700; }
  .service-band {
    position: absolute; left: 0; right: 0; top: 348px; height: 60px;
  }
  .service-band svg { position: absolute; inset: 0; width: 100%; height: 100%; }
  .service-label {
    position: absolute; left: 0; right: 0; top: 0; height: 60px;
    display: flex; align-items: center; justify-content: center;
    font-weight: 500; font-size: 30px; letter-spacing: 5px;
  }
  .sill-line {
    position: absolute; left: 320px; right: 240px; bottom: 22px; height: 14px;
    background: var(--ink); border-radius: 7px;
  }
</style>
</head>
<body>
<main class="sheet">

  <section class="wrap-panel wrap-panel--variant-a">
    <div class="brand">
      <span class="brand-name">PLIMTAAAB</span>
      <span class="brand-dot"></span>
    </div>
    <div class="contact">
      <p class="contact-phone">+41 41 555 01 23</p>
      <p class="contact-web">www.<strong>plimtaaab</strong>.ch</p>
    </div>
    <div class="service-band">
      <svg viewBox="0 0 1080 60" preserveAspectRatio="none" aria-hidden="true">
        <polygon points="150,0 38,0 0,60 150,60" fill="#e2c20e"/>
        <polygon points="250,0 930,0 900,60 220,60" fill="#ececec"/>
        <polygon points="182,0 212,0 182,60 152,60" fill="#161616"/>
        <polygon points="222,0 244,0 214,60 192,60" fill="#161616"/>
        <polygon points="936,0 958,0 988,60 966,60" fill="#161616"/>
        <polygon points="968,0 998,0 1028,60 998,60" fill="#161616"/>
      </svg>
      <p class="service-label">HAUSTECHNIK + BAUSPENGLEREI</p>
    </div>
    <div class="sill-line"></div>
  </section>

  <section class="wrap-panel wrap-panel--variant-b">
    <div class="brand">
      <span class="brand-name">PLIMTAAAB</span>
    </div>
    <div class="contact">
      <p class="contact-phone">+41 41 555 01 23</p>
      <p class="contact-web">www.<strong>plimtaaab</strong>.ch</p>
    </div>
    <div class="service-band">
      <svg viewBox="0 0 1080 60" preserveAspectRatio="none" aria-hidden="true">
        <polygon points="250,0 930,0 900,60 220,60" fill="#ececec"/>
        <polygon points="182,0 212,0 182,60 152,60" fill="#161616"/>
        <polygon points="222,0 244,0 214,60 192,60" fill="#161616"/>
        <polygon points="936,0 958,0 988,60 966,60" fill="#161616"/>
        <polygon points="968,0 998,0 1028,60 998,60" fill="#161616"/>
      </svg>
      <p class="service-label">HAUSTECHNIK + BAUSPENGLEREI</p>
    </div>
    <div class="sill-line"></div>
  </section>

</main>
</body>
</html>
```